Marta Gellworth Name Card Design

Hello Designers,
I wanna have a name card with these details below:
Name: Marta Gellworth
Job Title: Doctor
Address: 2318 Birch Lane, Tacoma, WA, US
Phone: 9517380294
Slogan on card: Health care 24/7, Whenever you need, we're there!
I love yellows colors, red and white. It would be nice if my card would be designed with these colors.

Doctor

```html
<!DOCTYPE html>
<html lang="en">
<head>
<meta charset="UTF-8">
<title>Marta Gellworth – Name Card</title>
<link rel="stylesheet" href="https://fonts.googleapis.com/css2?family=Lato:ital,wght@0,400;0,700;1,400&family=Oswald:wght@400&display=swap">
<style>
  :root {
    --card-bg: #ffffff;
    --ink: #343d44;
    --ink-muted: #6e7b7b;
    --band-red: #7a0000;
    --band-orange: #ff8c00;
    --slogan: #ffffff;
    --scope-dark: #3a3f44;
    --scope-light: #e4e6e8;
  }
  * { margin: 0; padding: 0; box-sizing: border-box; }
  html, body {
    width: 1200px;
    height: 686px;
    overflow: hidden;
    background: var(--card-bg);
  }
  .card {
    position: relative;
    width: 1200px;
    height: 686px;
    background: var(--card-bg);
    font-family: "Lato", sans-serif;
    color: var(--ink);
  }
  .holder-name {
    position: absolute;
    left: 43px;
    top: 40px;
    font-size: 51px;
    font-weight: 700;
    letter-spacing: 0.3px;
    line-height: 1;
  }
  .holder-role {
    position: absolute;
    left: 43px;
    top: 108px;
    font-size: 46px;
    font-style: italic;
    font-weight: 400;
    color: var(--ink-muted);
    line-height: 1;
  }
  .slogan-band {
    position: absolute;
    left: 0;
    top: 207px;
    width: 1200px;
    height: 205px;
    background: var(--band-red);
    display: flex;
    align-items: center;
    justify-content: center;
  }
  .slogan {
    font-family: "Oswald", sans-serif;
    font-weight: 400;
    font-size: 58px;
    color: var(--slogan);
    letter-spacing: 0.5px;
    white-space: nowrap;
  }
  .accent-band {
    position: absolute;
    left: 0;
    top: 412px;
    width: 1200px;
    height: 24px;
    background: var(--band-orange);
  }
  .contact {
    position: absolute;
    left: 43px;
    top: 540px;
    font-size: 41px;
    line-height: 51px;
    list-style: none;
  }
  .stethoscope-art {
    position: absolute;
    left: 890px;
    top: 447px;
    width: 263px;
    height: 187px;
    border-radius: 12px;
    background: linear-gradient(135deg, var(--scope-dark) 0%, #8a8f94 55%, var(--scope-light) 100%);
    opacity: 0.85;
  }
</style>
</head>
<body>
  <main class="card">
    <h1 class="holder-name">Marta Gellworth</h1>
    <p class="holder-role">Doctor</p>

    <section class="slogan-band">
      <p class="slogan">Health care 24/7, Whenever you need, we're there!</p>
    </section>
    <div class="accent-band"></div>

    <ul class="contact">
      <li class="contact-address">Address: 2318 Birch Lane, Tacoma, WA, US</li>
      <li class="contact-phone">Phone: 9517380294</li>
    </ul>

    <div class="stethoscope-art" role="img" aria-label="Illustration of a stethoscope"></div>
  </main>
</body>
</html>
```